Word Bureau Ostrelle Templates

We run a large number of businesses, including schools, airports, hotels and offices. We write reports on a daily basis and are looking for a strong and sexy WORD Template. We already have a logo in place (see graphical chart attached), that is rights' protected. We are looking for a beautiful wich reflect modern design and human aspects. Our logo has 2 design, full fill and watermark. It can be used in red or black.

Architects, Fire brigade, Building investors, contactors

• Arial, Calibri, ...

• Cover page, summary, Bullet points, Tables, Figures, Annex

```html
<!DOCTYPE html>
<html lang="en">
<head>
<meta charset="utf-8">
<title>Bureau Ostrelle – Report Cover Template</title>
<link rel="stylesheet" href="https://fonts.googleapis.com/css2?family=Lexend:wght@400;500&family=Roboto+Condensed:wght@400;700&display=swap">
<style>
  :root {
    --stage: #000000;
    --brand-red: #e8403a;
    --deep-red: #d10d0a;
    --wash-red: #d93a36;
    --band-grey: #3b3b3b;
    --paper: #ffffff;
    --ink: #1d1d1d;
    --ink-soft: #3a3a3a;
    --text-on-red: #ffffff;
  }
  * { box-sizing: border-box; margin: 0; padding: 0; }
  html, body {
    width: 1200px; height: 845px; overflow: hidden;
    background: var(--stage);
  }
  .spread { position: relative; width: 1200px; height: 845px; }
  .page {
    position: absolute; top: 14px; width: 576px; height: 817px;
    background: var(--paper); overflow: hidden;
  }
  .page--back { left: 14px; }
  .page--front { left: 603px; }
  .page__shapes { position: absolute; inset: 0; }
  .photo { position: absolute; }

  .intro {
    position: absolute; left: 44px; top: 66px; width: 283px;
    color: var(--text-on-red);
    font-family: "Roboto Condensed", sans-serif;
  }
  .intro__title { font-weight: 700; font-size: 12.5px; margin-bottom: 9px; }
  .intro__body { font-size: 8.6px; line-height: 1.55; text-align: justify; }

  .brand {
    position: absolute; display: flex; align-items: center; gap: 14px;
    font-family: "Lexend", sans-serif; color: var(--ink);
  }
  .brand__dot { width: 34px; height: 34px; border-radius: 50%; background: var(--brand-red); flex: none; }
  .brand__name { font-size: 32px; font-weight: 400; line-height: 1.08; }
  .page--back .brand { left: 40px; top: 553px; }
  .page--front .brand { right: 22px; top: 684px; }

  .address {
    position: absolute; left: 100px; top: 634px; list-style: none;
    font-family: "Lexend", sans-serif; font-size: 17px; color: var(--ink-soft);
  }
  .address li { line-height: 29px; }

  .project {
    position: absolute; right: 22px; top: 572px; text-align: right;
    font-family: "Lexend", sans-serif;
  }
  .project__title { font-size: 29px; font-weight: 400; color: var(--brand-red); line-height: 1.2; }
  .project__subtitle { font-size: 23px; font-weight: 400; color: var(--ink-soft); line-height: 1.3; }
</style>
</head>
<body>
<main class="spread">

  <section class="page page--back">
    <svg class="page__shapes" width="576" height="817" viewBox="0 0 576 817">
      <defs>
        <linearGradient id="industryWash" x1="0" y1="0" x2="0" y2="1">
          <stop offset="0" stop-color="#d93a36" stop-opacity="0"/>
          <stop offset="1" stop-color="#e6716c" stop-opacity="0.55"/>
        </linearGradient>
      </defs>
      <rect width="576" height="560" fill="var(--wash-red)"/>
      <rect class="photo" role="img" aria-label="Faint photograph of an industrial refinery skyline" x="0" y="180" width="576" height="380" fill="url(#industryWash)"/>
      <polygon points="0,436 576,540 576,560 0,456" fill="var(--band-grey)"/>
      <polygon points="0,449 576,553 576,817 0,817" fill="var(--paper)"/>
      <rect x="0" y="796" width="576" height="21" fill="var(--brand-red)"/>
    </svg>

    <article class="intro">
      <h2 class="intro__title">Paragraph Title here</h2>
      <p class="intro__body">In the past three years, our firm has not lost any nonprofit clients. Our five largest clients lost in that timeframe are all financial institutions that were acquired by another company that was not an existing client of the firm. We have not had any client retention issues that related to unresolved auditing or accounting matters. In the past three years, our firm has not lost any nonprofit clients. Our five largest clients lost in that timeframe are all financial institutions that were acquired by another company that was not an existing client of the firm. We have not had any client retention issues that related to unresolved auditing or accounting matters.</p>
    </article>

    <div class="brand">
      <span class="brand__dot"></span>
      <span class="brand__name">Bureau<br>Ostrelle</span>
    </div>

    <ul class="address">
      <li>Adress Line Text here</li>
      <li>Adress Line Text here</li>
      <li>Adress Line Text here</li>
    </ul>
  </section>

  <section class="page page--front">
    <svg class="page__shapes" width="576" height="817" viewBox="0 0 576 817">
      <defs>
        <radialGradient id="weldGlow" cx="0.5" cy="0.78" r="0.6">
          <stop offset="0" stop-color="#ff6a4a"/>
          <stop offset="0.35" stop-color="#e52414"/>
          <stop offset="1" stop-color="#c80806"/>
        </radialGradient>
      </defs>
      <rect class="photo" role="img" aria-label="Photograph of a welder in a protective mask working with sparks, tinted red" x="0" y="0" width="576" height="560" fill="url(#weldGlow)"/>
      <polygon points="0,543 576,445 576,465 0,563" fill="var(--band-grey)"/>
      <polygon points="0,555 576,457 576,817 0,817" fill="var(--paper)"/>
      <rect x="0" y="796" width="576" height="21" fill="var(--brand-red)"/>
    </svg>

    <header class="project">
      <h1 class="project__title">Project Title Here</h1>
      <p class="project__subtitle">Subtext here</p>
    </header>

    <div class="brand">
      <span class="brand__dot"></span>
      <span class="brand__name">Bureau<br>Ostrelle</span>
    </div>
  </section>

</main>
</body>
</html>
```